New startup requiring business card

New company needed a business card / logo. Company name is
Zuvrel
Company is providing IT software sales, partnering and consulting services across the APAC region. Catch line is "growing together".
We currently have a feeling yellow as the primary colour given its meaning across the region but open to ideas. Main brief is we want something smart, clean and professional while still leveraging the strength of the name.
A major part of the business is mutually beneficial partnerships, not sure if this helps but maybe visual around linkages between objects.
Also wanting a standard size card, preference is something that will have a D/S cello sheen finish in a matt. But again open to ideas, wow us!
Software

```html
<!DOCTYPE html>
<html lang="en">
<head>
<meta charset="utf-8">
<title>Zuvrel — Business Card</title>
<link href="https://fonts.googleapis.com/css2?family=Jost:wght@400&family=Michroma&display=swap" rel="stylesheet">
<style>
  :root {
    --backdrop: #34322f;
    --card-light: #2e2e2e;
    --card-dark: #1b1b1b;
    --brand-yellow: #ddd62a;
    --rule-grey: #9a9a9a;
    --text-white: #f1f1f1;
    --text-soft: #c9c9c9;
    --tagline-grey: #bdbdbd;
  }
  * { box-sizing: border-box; margin: 0; padding: 0; }
  html, body { width: 1200px; height: 900px; overflow: hidden; }
  body {
    position: relative;
    background: var(--backdrop);
    font-family: "Jost", "Futura", sans-serif;
  }
  .card {
    position: absolute;
    width: 409px;
    height: 708px;
    background: radial-gradient(ellipse at 50% 40%, var(--card-light) 0%, var(--card-dark) 85%);
    box-shadow: 0 10px 30px rgba(0,0,0,0.45);
  }
  .card--front { left: 112px; top: 70px; }
  .card--back  { left: 601px; top: 138px; }

  .rule { position: absolute; left: 19px; width: 3px; }
  .rule--grey { background: var(--rule-grey); }
  .rule--yellow { background: var(--brand-yellow); }

  .brand-dot {
    position: absolute;
    width: 70px; height: 70px;
    border-radius: 50%;
    background: var(--brand-yellow);
  }

  .wordmark {
    position: absolute;
    font-family: "Michroma", sans-serif;
    font-size: 38px;
    letter-spacing: 4px;
    line-height: 1;
    color: var(--brand-yellow);
    text-transform: uppercase;
    white-space: nowrap;
  }
  .tagline {
    position: absolute;
    font-family: "Michroma", sans-serif;
    font-size: 12.5px;
    letter-spacing: 4.3px;
    color: var(--tagline-grey);
    text-transform: uppercase;
    white-space: nowrap;
  }

  .person-name {
    position: absolute; left: 56px; top: 425px;
    font-size: 25px; color: var(--text-white);
  }
  .person-role {
    position: absolute; left: 56px; top: 461px;
    font-size: 21px; color: var(--text-soft);
  }
  .contact {
    position: absolute; right: 16px;
    display: flex; align-items: center; gap: 10px;
    font-size: 18px; color: var(--text-soft);
    letter-spacing: 0.5px;
  }
  .contact--phone { top: 540px; }
  .contact--email { top: 570px; font-size: 17px; }
  .contact svg { fill: none; stroke: var(--text-soft); stroke-width: 1.6; }

  .website {
    position: absolute; right: 28px; top: 665px;
    font-size: 19px; letter-spacing: 2.5px; color: var(--text-soft);
  }
  .website .website-name { color: var(--brand-yellow); text-transform: uppercase; letter-spacing: 3px; }
</style>
</head>
<body>

  <section class="card card--front">
    <div class="rule rule--grey" style="top:30px; height:470px;"></div>
    <div class="rule rule--yellow" style="top:500px; height:208px;"></div>

    <div class="brand-dot" style="left:169px; top:250px;"></div>
    <div class="wordmark" style="left:53px; top:485px;">Zuvrel</div>
    <div class="tagline" style="left:56px; top:526px;">Growing Together</div>
  </section>

  <section class="card card--back">
    <div class="rule rule--grey" style="top:0; height:355px;"></div>
    <div class="rule rule--yellow" style="top:355px; height:275px;"></div>
    <div class="rule rule--grey" style="top:630px; height:78px;"></div>

    <div class="brand-dot" style="left:170px; top:75px;"></div>
    <div class="wordmark" style="left:54px; top:298px;">Zuvrel</div>
    <div class="tagline" style="left:56px; top:338px;">Growing Together</div>

    <div class="person-name">Mara Ellison</div>
    <div class="person-role">Director</div>

    <div class="contact contact--phone">
      <svg width="14" height="24" viewBox="0 0 14 24" aria-hidden="true">
        <rect x="1" y="1" width="12" height="22" rx="2"/>
        <line x1="1" y1="4.5" x2="13" y2="4.5"/>
        <line x1="1" y1="18.5" x2="13" y2="18.5"/>
      </svg>
      <span>0198 765 432</span>
    </div>
    <div class="contact contact--email">
      <svg width="26" height="18" viewBox="0 0 26 18" aria-hidden="true">
        <rect x="1" y="1" width="24" height="16"/>
        <polyline points="1,1 13,10 25,1"/>
      </svg>
      <span>MaraEllison@zuvrel.com</span>
    </div>

    <div class="website">www.<span class="website-name">Zuvrel</span>.com</div>
  </section>

</body>
</html>
```